Bright Path Flyer Design for Virtual Online Clinic. -5.5 x 8.5 inches (half sheet)

We need a clean, modern flyer design for Bright Path, a new virtual walk-in clinic based in British Columbia. The flyer will be used in libraries, pharmacies, and community centers to help residents easily access primary care through their Bright Path NFC access card.
The flyer will ask a question : NEED A DOCTOR? This should be large and attention grabbing.
The design should clearly feature a Bright Path card image (the access card) as the centerpiece and visually show how patients can use it to book appointments. The tone should feel trustworthy, healthcare-oriented, and community-friendly — clean fonts, clear spacing, and strong readability from a distance.

Side One: This card has the NFC Access Card.
NEED A DOCTOR? (Large Font, Attention Grabbing)
How to Book an Appointment using your Bright Path Card
Step 1: Tap Your Card on Your Phone
Hold your card near the back of your phone.
It will activate automatically — no app needed.
The Bright Path scheduler will open.
Step 2: Schedule Your Appointment
Select your clinical concern.
Choose your time window.
Register (only once).
Confirm your appointment.
Step 3: Relax, we’ll take care of the rest
A doctor will call during your scheduled time.
Once booked, you’ll be able to call our office.
No emails, no texts — just a real person.
It’s that simple.
Side Two:
About Bright Path
Created by Dr. Marcus Ferrigan
Bright Path was founded to make healthcare simple and convenient. Prescription renewals. Common infections. Medical notes. And so much more.
Our doctors can address 120+ health concerns virtually — providing quality care without the waiting room. No waiting rooms. Just real doctors providing real care.
Why Patients Choose Bright Path
Easy access – book and be seen from anywhere in BC.
Effortless booking – tap your Bright Path Card to begin.
Trusted physicians – every visit is with a licensed BC family doctor.
How It Works
Book your visit — choose a time window that fits your day.
Join the queue — you’ll be called when it’s your turn.
Speak directly with your doctor — simple, secure, and stress-free.
Convenient Care for Common Concerns

Additional Details.
Please find the domain to be launched soon. I've attached the NFC card file for review, it is 85.5 mm x 54 mm. The card will be glued to the flyer.
I've attached examples of flyers but they are not the look I am seeking and I am looking for creative solutions.
Thank you!
http://brightpath-example.test/

Adult Patients in British Columbia

Healthcare

• Looking for clean lines, uniform appearance, and high legibility i.e poppins

0054AA
0677BA
7BADD7
CADEEF
E8F1F8

• Need A Doctor?
• Elegant style, not too busy, clear layout.
• Clutter, look cheap - review examples.

```html
<!DOCTYPE html>
<html lang="en">
<head>
<meta charset="utf-8">
<title>Bright Path – Half Sheet Flyer, Double Sided</title>
<link href="https://fonts.googleapis.com/css2?family=Poppins:wght@300;400;500;600;700&display=swap" rel="stylesheet">
<style>
:root{
  --board:#d6d6d6;
  --paper:#ffffff;
  --teal:#14a89a;
  --navy:#2a448a;
  --sky:#7badd7;
  --ink:#3a3a3a;
  --rule:#333333;
}
*{margin:0;padding:0;box-sizing:border-box}
html,body{width:1200px;height:1200px;overflow:hidden;background:var(--board);font-family:'Poppins',sans-serif;color:var(--ink)}
.board{position:relative;width:1200px;height:1200px}
.board-caption{position:absolute;top:104px;left:0;width:1200px;text-align:center;font-weight:300;font-size:19px;line-height:22px;color:#222}
.flyer{position:absolute;top:190px;height:786px;background:var(--paper);overflow:hidden}
.flyer--front{left:74px;width:508px}
.flyer--back{left:624px;width:510px}
.abs{position:absolute}
.center{left:0;right:0;text-align:center}

/* front */
.headline{top:32px;font-weight:700;font-size:77px;line-height:66px;color:var(--teal);letter-spacing:-1px}
.subhead{top:175px;font-weight:600;font-size:18.5px;line-height:27px;color:var(--navy)}
.card-label{top:255px;left:98px;width:312px;display:flex;align-items:center;gap:8px;font-size:12px;line-height:18px;color:var(--ink)}
.card-label::before,.card-label::after{content:"";flex:1;height:1px;background:var(--rule)}
.access-card{top:285px;left:98px;width:312px;height:197px;border-radius:12px;background:var(--navy);display:flex;flex-direction:column;align-items:center;justify-content:center;color:#fff}
.access-card__name{font-weight:500;font-size:28px;line-height:36px;display:flex;align-items:center;gap:8px}
.access-card__dot{width:10px;height:10px;border-radius:50%;background:#fff}
.access-card__url{margin-top:8px;font-size:10px;letter-spacing:.5px}
.step{width:240px}
.step__num{font-weight:600;font-size:12px;line-height:17px;color:var(--teal)}
.step__title{font-weight:600;font-size:12px;line-height:17px;color:var(--navy)}
.step ul{list-style:none;font-weight:300;font-size:11px;line-height:16.8px;color:var(--ink)}
.step li{padding-left:7px;text-indent:-7px}
.step li::before{content:"• "}
.step--one{left:43px;top:501px}
.step--two{left:297px;top:501px}
.step--three{left:135px;top:619px;width:260px}
.footer-rule{left:0;right:0;top:739px;height:1px;background:var(--teal)}
.footer-pill{top:727px;height:25px;border-radius:13px;background:var(--teal);color:#fff;font-size:14px;line-height:25px;text-align:center}
.footer-pill--front{left:170px;width:144px}
.footer-pill--back{left:104px;width:301px}

/* back */
.hero-band{top:0;left:0}
.about-label{top:60px;font-size:16px;line-height:20px;color:#fff}
.brand-mark{top:104px;font-weight:500;font-size:46px;line-height:50px;color:#fff;display:flex;justify-content:center;align-items:center;gap:12px}
.brand-mark__dot{width:14px;height:14px;border-radius:50%;background:#fff}
.created-by{top:179px;font-size:16px;line-height:20px;color:var(--sky)}
.founder{top:202px;font-weight:600;font-size:16px;line-height:20px;color:#fff}
.intro{top:297px;font-weight:300;font-size:11px;line-height:18px;color:var(--ink)}
.intro strong{font-weight:600;color:var(--navy)}
.intro--second{top:375px}
.tag{top:419px;height:23px;border:1.5px solid var(--teal);border-radius:12px;font-weight:300;font-size:11px;line-height:20px;text-align:center;color:var(--ink)}
.tag--one{left:90px;width:114px}
.tag--two{left:213px;width:207px}
.feature{left:76px;width:420px}
.feature h2{font-weight:600;font-size:12.5px;line-height:18px;color:var(--navy)}
.feature ul{list-style:none;font-weight:300;font-size:11px;line-height:18px;color:var(--ink)}
.feature li{display:flex;align-items:center;gap:6px}
.feature li svg{flex:none}
.feature--why{top:470px}
.feature--how{top:566px}
</style>
</head>
<body>
<div class="board">
  <p class="board-caption">Half Sheet Flyer<br>Double sided</p>

  <section class="flyer flyer--front">
    <h1 class="abs center headline">NEED<br>A DOCTOR?</h1>
    <p class="abs center subhead">How to Book an Appointment<br>using your Bright Path Card</p>
    <p class="abs card-label">This card has the NFC Access Card</p>
    <div class="abs access-card" role="img" aria-label="Bright Path NFC access card in navy">
      <span class="access-card__name"><span class="access-card__dot"></span>Bright Path</span>
      <span class="access-card__url">brightpath-example.test</span>
    </div>

    <div class="abs step step--one">
      <p class="step__num">Step 1:</p>
      <p class="step__title">Tap Your Card on Your Phone</p>
      <ul>
        <li>Hold your card near the back of your phone.</li>
        <li>It will activate automatically — no app needed.</li>
        <li>The Bright Path scheduler will open.</li>
      </ul>
    </div>
    <div class="abs step step--two">
      <p class="step__num">Step 2:</p>
      <p class="step__title">Schedule Your Appointment</p>
      <ul>
        <li>Select your clinical concern.</li>
        <li>Choose your time window.</li>
        <li>Register (only once).</li>
        <li>Confirm your appointment.</li>
      </ul>
    </div>
    <div class="abs step step--three">
      <p class="step__num">Step 3:</p>
      <p class="step__title">Relax, we’ll take care of the rest</p>
      <ul>
        <li>A doctor will call during your scheduled time.</li>
        <li>Once booked, you’ll be able to call our office.</li>
        <li>No emails, no texts — just a real person.</li>
      </ul>
    </div>

    <div class="abs footer-rule"></div>
    <p class="abs footer-pill footer-pill--front">It’s that Simple</p>
  </section>

  <section class="flyer flyer--back">
    <svg class="abs hero-band" width="510" height="270" viewBox="0 0 510 270" aria-hidden="true">
      <path d="M0 0H510V189Q255 341 0 189Z" fill="var(--navy)"/>
    </svg>
    <p class="abs center about-label">About</p>
    <p class="abs center brand-mark">Bright Path<span class="brand-mark__dot"></span></p>
    <p class="abs center created-by">Created by</p>
    <p class="abs center founder">Dr. Marcus Ferrigan</p>

    <p class="abs center intro"><strong>Bright Path</strong> was founded to make healthcare simple and convenient.<br>Prescription renewals, Common infections, Medical notes,<br>And so much more.</p>
    <p class="abs center intro intro--second">Our doctors can address 120+ health concerns virtually —<br>providing quality care without the waiting room.</p>
    <p class="abs tag tag--one">No waiting rooms.</p>
    <p class="abs tag tag--two">Just real doctors providing real care.</p>

    <div class="abs feature feature--why">
      <h2>Why patients choose Bright Path</h2>
      <ul>
        <li><svg width="9" height="8" viewBox="0 0 9 8"><path d="M1 4.2L3.3 6.5 8 1.2" fill="none" stroke="var(--teal)" stroke-width="1.6"/></svg>Easy access — book and be seen from anywhere in BC.</li>
        <li><svg width="9" height="8" viewBox="0 0 9 8"><path d="M1 4.2L3.3 6.5 8 1.2" fill="none" stroke="var(--teal)" stroke-width="1.6"/></svg>Effortless booking — tap your Bright Path card to begin.</li>
        <li><svg width="9" height="8" viewBox="0 0 9 8"><path d="M1 4.2L3.3 6.5 8 1.2" fill="none" stroke="var(--teal)" stroke-width="1.6"/></svg>Trusted physicians — every visit is with a licensed BC family doctor.</li>
      </ul>
    </div>
    <div class="abs feature feature--how">
      <h2>How it works</h2>
      <ul>
        <li><svg width="9" height="8" viewBox="0 0 9 8"><path d="M1 4.2L3.3 6.5 8 1.2" fill="none" stroke="var(--teal)" stroke-width="1.6"/></svg>Book your visit — choose a time window that fits your day.</li>
        <li><svg width="9" height="8" viewBox="0 0 9 8"><path d="M1 4.2L3.3 6.5 8 1.2" fill="none" stroke="var(--teal)" stroke-width="1.6"/></svg>Join the queue — you’ll be called when it’s your turn.</li>
        <li><svg width="9" height="8" viewBox="0 0 9 8"><path d="M1 4.2L3.3 6.5 8 1.2" fill="none" stroke="var(--teal)" stroke-width="1.6"/></svg>Speak directly with your doctor — simple, secure, and stress-free.</li>
      </ul>
    </div>

    <div class="abs footer-rule"></div>
    <p class="abs footer-pill footer-pill--back">Convenient Care for Common Concerns</p>
  </section>
</div>
</body>
</html>
```